Create a flyer for our party getaway to Ibiza.

'The Crimson Ibiza Escape'

Friday 14th July - Monday 17th July

DJ Morvek & DJ Tundral brings together a jam-packed weekend schedule full of the best urban parties in Ibiza.

What's included?

4 Nights Of Entertainment
6 Parties In Total
1 Boat Party
1 Pool Party
2 Superclub Parties
1 Indoor Water Party
Bottomless Drinks (Boat Party Only)
An unbelievable experience
1 unbeatable price.

All this for 140€ (you save 50€ when you book with us)

Tickets avaialble from Ticketlane & Gribolo

Target Market(s)

holiday goers

Industry/Entity Type

party, events, club, hip hop

Requirements
Must have
• good vibes
Nice to have
• nice catchy looking title

```html
<!DOCTYPE html>
<html lang="en">
<head>
<meta charset="utf-8">
<title>The Crimson Ibiza Escape</title>
<link rel="stylesheet" href="https://fonts.googleapis.com/css2?family=Archivo+Black&family=Barlow+Condensed:wght@500;600&family=Jost:wght@400;500&family=Oswald:wght@400;500&display=swap">
<style>
  :root {
    --stage: #1c1c1c;
    --yellow: #f7e21a;
    --yellow-deep: #e9c90f;
    --panel: #333333;
    --ink: #0c0c0c;
    --white: #ffffff;
    --crimson: #e0123f;
    --crimson-deep: #b80d2e;
    --orange: #f26a21;
  }
  * { margin: 0; padding: 0; box-sizing: border-box; }
  html, body { width: 1200px; height: 906px; overflow: hidden; background: var(--stage); }
  .poster {
    position: absolute; left: 302px; top: 23px; width: 596px; height: 860px;
    overflow: hidden; background: var(--yellow);
  }
  .backdrop {
    position: absolute; inset: 0;
    background: linear-gradient(180deg, var(--yellow-deep) 0%, var(--yellow) 45%, #f0d414 65%, var(--yellow) 100%);
  }
  .dj-photo {
    position: absolute; left: 125px; top: 225px; width: 348px; height: 170px; z-index: 1;
    background: linear-gradient(180deg, #5a5a5a 0%, #8a8a8a 40%, #d9d9d9 75%, #4f7a35 100%);
  }
  .title-panel {
    position: absolute; left: 65px; top: 10px; width: 467px; height: 215px; z-index: 2;
    background: var(--panel); color: var(--white);
    display: flex; flex-direction: column; align-items: center; justify-content: center;
    font-family: "Archivo Black", sans-serif; line-height: 1; overflow: hidden;
  }
  .title-panel .line-top { font-size: 54px; line-height: 58px; }
  .title-panel .line-mid {
    display: inline-block; font-size: 92px; line-height: 84px; transform: scaleX(1.45);
    color: var(--crimson);
    background: linear-gradient(180deg, #ff2f5a, var(--crimson-deep));
    -webkit-background-clip: text; background-clip: text; -webkit-text-fill-color: transparent;
  }
  .title-panel .line-bottom { font-size: 56px; line-height: 60px; letter-spacing: 20px; padding-left: 20px; }
  .dates {
    position: absolute; left: 0; top: 258px; width: 125px; height: 104px; z-index: 2;
    background: var(--ink); padding: 6px 0 0 13px;
    font-family: "Barlow Condensed", sans-serif; font-weight: 600; line-height: 1;
  }
  .dates .day { color: var(--white); font-size: 22px; }
  .dates .date { color: var(--crimson); font-size: 17px; margin-top: 1px; }
  .dates .rule { width: 100px; height: 2px; background: var(--crimson); margin: 6px 0 6px; }
  .headline {
    position: absolute; left: 104px; top: 378px; width: 410px; height: 190px; z-index: 3;
    background: var(--ink); transform: rotate(-5.5deg); color: var(--white);
    padding: 10px 12px 0; text-align: center; line-height: 1;
  }
  .headline .djs {
    font-family: "Archivo Black", sans-serif; font-size: 25px;
    border-bottom: 2px solid var(--white); padding-bottom: 4px; white-space: nowrap;
  }
  .headline .djs .amp { font-family: "Jost", sans-serif; font-weight: 500; }
  .headline .copy { font-family: "Jost", sans-serif; font-size: 23px; margin-top: 3px; white-space: nowrap; }
  .headline .strong { font-family: "Archivo Black", sans-serif; font-size: 24px; margin-top: 2px; white-space: nowrap; }
  .headline .place {
    font-family: "Archivo Black", sans-serif; font-size: 58px; line-height: 64px;
    text-align: left; padding-left: 8px; white-space: nowrap;
  }
  .headline .place .word-red {
    display: inline-block; color: var(--crimson); margin-left: 22px;
    transform: scaleX(1.3); transform-origin: left center;
  }
  .included {
    position: absolute; left: 0; right: 0; top: 598px; text-align: center;
    font-family: "Oswald", sans-serif; color: var(--ink);
  }
  .included .label {
    display: inline-block; background: var(--ink); color: var(--white);
    font-size: 13px; font-weight: 500; padding: 2px 9px; line-height: 17px;
  }
  .included ul { list-style: none; margin-top: 6px; font-size: 14px; line-height: 24px; }
  .price {
    position: absolute; left: 204px; top: 725px; width: 189px; height: 31px;
    background: var(--crimson); color: var(--white); text-align: center;
    font-family: "Oswald", sans-serif; font-weight: 500; font-size: 19px; line-height: 31px;
  }
  .saving {
    position: absolute; left: 0; right: 0; top: 764px; text-align: center;
    font-family: "Oswald", sans-serif; font-size: 10px; color: var(--ink);
  }
  .tickets {
    position: absolute; left: 49px; top: 810px; display: flex; align-items: center;
    font-family: "Archivo Black", sans-serif; color: var(--ink);
  }
  .tickets .lead { font-family: "Jost", sans-serif; font-weight: 500; font-size: 10px; letter-spacing: 1px; width: 175px; }
  .tickets .vendor { font-size: 26px; }
  .tickets .vendor + .vendor { margin-left: 28px; display: flex; align-items: center; }
  .tickets .mark { width: 14px; height: 14px; background: var(--orange); margin-right: 7px; }
</style>
</head>
<body>
  <div class="poster">
    <div class="backdrop" role="img" aria-label="Yellow-tinted photo of palm fronds over the Ibiza coastline and sea"></div>

    <div class="dj-photo" role="img" aria-label="Photo of the two DJs posing between stacked speakers with palm leaves below"></div>

    <div class="title-panel">
      <div class="line-top">THE CRIMSON</div>
      <div class="line-mid">IBIZA</div>
      <div class="line-bottom">ESCAPE</div>
    </div>

    <div class="dates">
      <div class="day">FRIDAY</div>
      <div class="date">14TH JULY</div>
      <div class="rule"></div>
      <div class="day">MONDAY</div>
      <div class="date">17TH JULY</div>
    </div>

    <div class="headline">
      <div class="djs">DJ MORVEK <span class="amp">&amp;</span> DJ TUNDRAL</div>
      <div class="copy">BRINGS TOGETHER A JAM-PACKED</div>
      <div class="copy">WEEKEND SCHEDULE FULL OF</div>
      <div class="strong">THE BEST URBAN PARTIES</div>
      <div class="place">IN<span class="word-red">IBIZA</span></div>
    </div>

    <div class="included">
      <div class="label">WHAT'S INCLUDED?</div>
      <ul>
        <li>4 NIGHTS OF ENTERTAINMENT &nbsp;|&nbsp; 6 PARTIES IN TOTAL &nbsp;|&nbsp; 1 BOAT PARTY</li>
        <li>1 POOL PARTY &nbsp;|&nbsp; 2 SUPERCLUB PARTIES &nbsp;|&nbsp; 1 INDOOR WATER PARTY</li>
        <li>BOTTOMLESS DRINKS (BOAT PARTY ONLY) AN UNBELIEVABLE EXPERIENCE</li>
        <li>1 UNBEATABLE PRICE.</li>
      </ul>
    </div>

    <div class="price">ALL THIS FOR 140€</div>
    <div class="saving">(YOU SAVE 50€ WHEN YOU BOOK WITH US)</div>

    <div class="tickets">
      <span class="lead">TICKETS AVAIALBLE FROM:</span>
      <span class="vendor">Gribolo</span>
      <span class="vendor"><span class="mark"></span>Ticketlane</span>
    </div>
  </div>
</body>
</html>
```